Bright Path Therapies business cards and stationary

Need business cards and stationary designed to match previously made logo for for a new company based in Sydney NSW called 'Bright Path Therapies'.

We provide early intervention services and diagnostic assessment for children with disability and their families. I would like designs that are colourful and child friendly - possibly using feet/footprints/steps on a white background. The final design should communicate that we are family friendly, accepting and fun to work with.

Target Market(s)

Parents and Families
Teachers
Allied Health Professionals

Industry/Entity Type

Psychology

Contact Information for Business Card

Bright Path Therapies
www.brightpaththerapies.example
info@brightpaththerapies.example

Font styles to use
Sans Serif
Decorative
Script

Requirements
Must have
• Match the font and colour scheme of logo, along with footprint picture
Nice to have
• Clean and simple, while reflecting that I am working with families.
• Also- editable for when we make staff specific cards.

```html
<!DOCTYPE html>
<html lang="en">
<head>
<meta charset="utf-8">
<title>Bright Path Therapies – Business Cards</title>
<link href="https://fonts.googleapis.com/css2?family=Amatic+SC:wght@700&family=Montserrat:wght@400;500&display=swap" rel="stylesheet">
<style>
  :root {
    --bg: #1c1c1e;
    --card: #141414;
    --coral: #ee4a3c;
    --orange: #f7931e;
    --green: #8cc63f;
    --blue: #2f7fc1;
    --white: #f2f2f2;
    --muted: #d8d8d8;
  }
  * { box-sizing: border-box; margin: 0; padding: 0; }
  html, body { width: 1200px; height: 900px; overflow: hidden; }
  body {
    background: var(--bg);
    font-family: "Montserrat", sans-serif;
    position: relative;
  }
  .card {
    position: absolute;
    left: 250px;
    width: 700px;
    height: 400px;
    background: var(--card);
    box-shadow: 0 10px 30px rgba(0,0,0,.55);
  }
  .card--front { top: 34px; }
  .card--back { top: 466px; }

  .brand {
    display: flex;
    align-items: center;
    gap: 16px;
  }
  .brand__dot {
    border-radius: 50%;
    background: var(--coral);
    flex: none;
  }
  .brand__name {
    font-family: "Amatic SC", sans-serif;
    font-weight: 700;
    line-height: .95;
    letter-spacing: 2px;
  }

  .card--front .brand {
    position: absolute;
    left: 50%; top: 50%;
    transform: translate(-50%, -50%);
  }
  .card--front .brand__dot { width: 78px; height: 78px; }
  .card--front .brand__name { font-size: 56px; color: var(--orange); }

  .card--back .brand {
    position: absolute;
    left: 44px; top: 50%;
    transform: translateY(-50%);
  }
  .card--back .brand__dot { width: 62px; height: 62px; }
  .card--back .brand__name { font-size: 44px; color: var(--blue); }

  .divider {
    position: absolute;
    left: 330px; top: 122px;
    width: 2px; height: 156px;
    background: var(--green);
  }
  .details {
    position: absolute;
    left: 356px; top: 116px;
  }
  .details__name {
    font-family: "Amatic SC", sans-serif;
    font-weight: 700;
    color: var(--green);
    font-size: 40px;
    letter-spacing: 2px;
    line-height: 1;
  }
  .details__role {
    color: var(--white);
    font-size: 16px;
    font-weight: 500;
    margin: 2px 0 16px;
  }
  .contact { list-style: none; }
  .contact li {
    display: flex;
    align-items: center;
    gap: 14px;
    color: var(--muted);
    font-size: 15px;
    line-height: 26px;
  }
  .contact svg { width: 15px; height: 15px; flex: none; }
  .contact .accent { color: var(--blue); }
</style>
</head>
<body>
  <section class="card card--front" aria-label="Business card front">
    <div class="brand">
      <span class="brand__dot"></span>
      <span class="brand__name">Bright Path<br>Therapies</span>
    </div>
  </section>

  <section class="card card--back" aria-label="Business card back">
    <div class="brand">
      <span class="brand__dot"></span>
      <span class="brand__name">Bright Path<br>Therapies</span>
    </div>
    <div class="divider"></div>
    <div class="details">
      <p class="details__name">Marcus J. Hale</p>
      <p class="details__role">Founder</p>
      <ul class="contact">
        <li>
          <svg viewBox="0 0 14 14" aria-hidden="true"><rect x="3.5" y="1" width="7" height="12" rx="1.2" fill="none" stroke="#ee4a3c" stroke-width="1.4"/><line x1="6" y1="11" x2="8" y2="11" stroke="#ee4a3c" stroke-width="1.2"/></svg>
          555-014-2290
        </li>
        <li>
          <svg viewBox="0 0 14 14" aria-hidden="true"><rect x="1" y="3" width="12" height="8" fill="none" stroke="#ee4a3c" stroke-width="1.4"/><polyline points="1,3 7,8 13,3" fill="none" stroke="#ee4a3c" stroke-width="1.4"/></svg>
          info@brightpaththerapies.example
        </li>
        <li>
          <svg viewBox="0 0 14 14" aria-hidden="true"><circle cx="7" cy="7" r="5.8" fill="none" stroke="#ee4a3c" stroke-width="1.3"/><ellipse cx="7" cy="7" rx="2.5" ry="5.8" fill="none" stroke="#ee4a3c" stroke-width="1.1"/><line x1="1.2" y1="7" x2="12.8" y2="7" stroke="#ee4a3c" stroke-width="1.1"/></svg>
          <span>www.<span class="accent">brightpaththerapies</span>.example</span>
        </li>
      </ul>
    </div>
  </section>
</body>
</html>
```